依頼詳細
上記に記載したアドバイスシートのベースを作成していただきたいです。内容は、顧客別に写真を入れたり、文字を入れたりするので、データで納品していただきたいです。30代、40代がメインターゲットで、おしゃれで少しラグジュアリーかつ女性らしいデザインを希望します。
内容や順番などこちらも変更する可能性があります。現在使っているアドバイスシートを参考にオシャレに、気分が上がるような仕上がりにしていただくのが希望です。 通常、初回の体験を受けていただいたお客様にはレッスンに進む方も多いのですが、こちらの方々にもノートというか、教科書のようなものを今後作成したいと思っているので、今回のデザインとも統一感を持たせたいと思っているので、お願いする可能性もあるかもしれません。
サイズ
A4
ページ数
10ページ
希望イメージ
シンプル 複雑
単色 カラフル
暗い 明るい
日常 高級
遊び心 厳粛
未来的 伝統的
女性的 男性的
希望する色
メイクアップと言って想像するような色、単色よりは数色使ってバランスの良い感じ
納品ファイル
補足説明
添付しているものが現在使用しているアドバイスシートです。これにもっと情報を追加していきたいので、添付しているものよりページ数などは増えると思います。(追加する文章や情報などは現在作成中です) 。デザインや、文字の配置、分かりやすさなどを追求したいので、そのあたりはアドバイスをいただけると有り難いです。現在、ベースのアドバイスシートをgood notesに取り込んで、iPadで文字と写真、写真への書き加えはペンで書き加えています。ですがこの作業が結構時間がかかって仕事量として重たいので、何かいいやり方があればそれもアドバイスいただけると嬉しいです。
内容は何度もやりとりして修正させていただく可能性があるので、一旦大幅であっても、早めに出していただけると決めやすいです。・最初のデザインの全体的な雰囲気や、ご提案者様の過去の事例など見させていただき雰囲気を決めさせていただきたいです。・あと、こちらからの希望になるべく沿っていただけるようやりとりしていただける方がとても有り難いです。当方今月より産休に入っており、日中も時間は割とあるので、ご対応していただけると助かります。(募集最終日頃にかなり決めた形で作り込んで応募される方よりは、最初はラフな形から今後柔軟に対応していただける方の方がありがたいです) 基本は作成枚数によって価格を決めさせていただきたいと思っています。現状より増える可能性が高いので、価格は上がる可能性があります。
ご応募ありがとうございます。追加修正の依頼を記載いたします。
【現在依頼しているページについて】
・ビフォーアフターや、各種メイク工程のページについて、文字量が多くみづらいのが難点で、もう少しグラフや表を入れて可視化したいです。(アイディアがあればお願いします) 添付PDF1枚目

【追加ページについて】
・お悩みとなりたいイメージを記載するページ(こちらも表やグラフなどで可視化できる案があればありがたいです)添付PDF2枚目

・添付PDF3枚目
利用サービスの流れを可視化できるページを作成したいです

・添付PDF4枚目
サロンの情報へアクセスできるよう情報をまとめたページ

今後メイクやスキンケア販売をしたい方へ向けての告知ページ

一旦以上になります。
すみません。募集が終了した場合添付ができないかもしれず、現在調べております。もしできない場合は、選定させていただき、個別にご連絡させていただきます。
可能な場合はPDF添付させていただきます。

依頼に加え、提案などしていただいたのでとても有り難かったです。

皆様とても魅力的なご提案ばかりで、ギリギリまで選定できず申し訳ございませんでした。今回は1社に決めさせていただいたのですが、素敵なご提案ばかりで、お願いして良かったなと思いました。こちらのご提案にお時間や尽力を割いていただいてありがとうございました。また機会ありましたらよろしくお願いいたします。

```html
<!DOCTYPE html>
<html lang="ja">
<head>
<meta charset="utf-8">
<title>make advice sheet</title>
<link href="https://fonts.googleapis.com/css2?family=Great+Vibes&family=Cormorant+Garamond:ital,wght@0,500;1,500&family=Noto+Serif+JP:wght@400;500&family=Noto+Sans+JP:wght@400;500&display=swap" rel="stylesheet">
<style>
  :root {
    --paper: #ffffff;
    --frame-outer: #d9c7e6;
    --frame-inner: #f0c6d3;
    --rose: #e59bb4;
    --rose-soft: #f8dbe5;
    --lavender: #9b86b8;
    --ink: #4a4446;
    --photo-a: #d9cfcb;
    --photo-b: #e2dad7;
  }
  * { margin: 0; padding: 0; box-sizing: border-box; }
  html, body { width: 845px; height: 1200px; overflow: hidden; background: var(--paper); }
  .sheet {
    position: relative; width: 845px; height: 1200px; background: var(--paper);
    font-family: "Noto Sans JP", sans-serif; color: var(--ink);
  }
  .frame-outer { position: absolute; inset: 10px; border: 2px solid var(--frame-outer); }
  .frame-inner { position: absolute; inset: 20px; border: 1px solid var(--frame-inner); }
  .badge {
    position: absolute; left: 22px; top: 6px; width: 46px; height: 46px; border-radius: 50%;
    background: var(--rose); color: #fff; font-family: "Noto Serif JP", serif;
    font-size: 11px; line-height: 1.15; display: flex; align-items: center; justify-content: center;
    text-align: center;
  }
  .sheet-title {
    position: absolute; left: 205px; top: 14px; font-family: "Cormorant Garamond", serif;
    font-style: italic; font-size: 36px; color: var(--lavender); letter-spacing: 1px;
  }
  .title-rule { position: absolute; left: 200px; right: 40px; top: 62px; height: 1px; background: var(--frame-inner); }
  .client-name {
    position: absolute; left: 575px; top: 66px; font-family: "Noto Serif JP", serif;
    font-size: 22px; letter-spacing: 2px;
  }
  .client-name small { font-size: 15px; margin-left: 8px; }
  .view-label {
    position: absolute; font-family: "Great Vibes", cursive; font-size: 40px; color: var(--rose); line-height: 1;
  }
  .photo { position: absolute; }
  .photo-front { left: 62px; top: 290px; width: 333px; height: 430px; background: linear-gradient(180deg, var(--photo-b), var(--photo-a)); }
  .photo-right { left: 418px; top: 176px; width: 382px; height: 298px; background: linear-gradient(180deg, var(--photo-b), var(--photo-a)); }
  .photo-left { left: 418px; top: 528px; width: 382px; height: 222px; background: linear-gradient(180deg, var(--photo-b), var(--photo-a)); }
  .note { position: absolute; }
  .note-head { display: flex; align-items: center; gap: 14px; }
  .note-mark {
    position: relative; width: 64px; height: 64px; border-radius: 50%; background: var(--rose-soft);
    font-family: "Great Vibes", cursive; font-size: 52px; color: var(--rose); line-height: 64px; text-align: center;
  }
  .note-title { font-family: "Noto Serif JP", serif; font-size: 20px; color: var(--ink); }
  .note-body { font-size: 13.5px; line-height: 1.95; margin-top: 14px; }
  .note-front { left: 62px; top: 850px; width: 340px; }
  .note-right { left: 430px; top: 810px; width: 370px; }
  .note-left { left: 430px; top: 930px; width: 370px; }
  .note-right .note-body, .note-left .note-body { margin-top: 6px; }
  .salon-mark {
    position: absolute; left: 690px; top: 1110px; display: flex; align-items: center; gap: 6px;
    font-family: "Noto Sans JP", sans-serif; font-size: 12px; color: var(--lavender);
  }
  .salon-mark i { display: block; width: 10px; height: 10px; border-radius: 50%; background: var(--lavender); }
</style>
</head>
<body>
<main class="sheet">
  <div class="frame-outer"></div>
  <div class="frame-inner"></div>

  <div class="badge">骨格<br>分析</div>
  <h1 class="sheet-title">make advice sheet</h1>
  <div class="title-rule"></div>
  <p class="client-name">佐藤 美咲<small>様</small></p>

  <span class="view-label" style="left:62px;top:246px;">A</span>
  <div class="photo photo-front" role="img" aria-label="正面の顔写真と骨格分析の線"></div>

  <span class="view-label" style="left:418px;top:134px;">B</span>
  <div class="photo photo-right" role="img" aria-label="右顔の写真と骨格分析の線"></div>

  <span class="view-label" style="left:418px;top:486px;">C</span>
  <div class="photo photo-left" role="img" aria-label="左顔の写真と骨格分析の線"></div>

  <section class="note note-front">
    <div class="note-head"><span class="note-mark">A</span><h2 class="note-title">全体</h2></div>
    <p class="note-body">輪郭はかっちりとした印象。パーツはつり目さん（左）の要素以外は、配置を寄せると、可愛く若々しく見える要素が多いです。<br>目元を横へ縦に大きく見せる事と、ハイライトを効果的に使う事でパーツの大きさと輪郭の広さのバランスが◎に！</p>
  </section>

  <section class="note note-right">
    <div class="note-head"><span class="note-mark">B</span><h2 class="note-title">右顔</h2></div>
    <p class="note-body">右側の顔はバランスが良いです。目も大きく、チークなど思うように入れやすいです。</p>
  </section>

  <section class="note note-left">
    <div class="note-head"><span class="note-mark">C</span><h2 class="note-title">左顔</h2></div>
    <p class="note-body">左は骨ばった印象が強く、眉・目元が上がって見えやすく口角は逆です。右側に合わせてメイクをするようにしましょう！</p>
  </section>

  <div class="salon-mark"><i></i>Lumière Salon</div>
</main>
</body>
</html>
```